Brennick Construction Core Values Wall Design

Core Values Wall Design for our Wall, I’m not exactly sure visually what we would want it to look like. Maybe some acrylic stand offs that could go on brick? If that’s a possibility. That’s where we have the most space in the office. But we could do other locations too.

These are our core values
• Safety
• Integrity
• Quality
• Client-Focused Solutions
• Continuous Improvement
• Positive Culture and Stewardship

Our vision/mission statement is Excellence Delivered.

```html
<!DOCTYPE html>
<html lang="en">
<head>
<meta charset="utf-8">
<title>Brennick Construction – Core Values Wall</title>
<link href="https://fonts.googleapis.com/css2?family=Poppins:wght@600;700&display=swap" rel="stylesheet">
<style>
  :root {
    --canvas-bg: #2e323c;
    --header-top: #6d727b;
    --header-bottom: #3f4751;
    --blue-light: #62c8f2;
    --blue-dark: #1568ab;
    --blue-fold-top: #2a8ccc;
    --blue-fold-bottom: #0e4d86;
    --red-light: #f5a8a8;
    --red-dark: #e5262f;
    --red-fold-top: #f07a7e;
    --red-fold-bottom: #c41c25;
    --text-light: #ffffff;
  }
  html, body {
    margin: 0;
    padding: 0;
    width: 1200px;
    height: 680px;
    overflow: hidden;
    background: var(--canvas-bg);
  }
  .wall-canvas {
    width: 1200px;
    height: 680px;
    display: flex;
    align-items: center;
    justify-content: center;
  }
  .values-sign {
    height: 630px;
    width: auto;
    display: block;
  }
  .values-sign text {
    font-family: "Poppins", sans-serif;
    fill: var(--text-light);
    text-anchor: middle;
  }
  .mission-text { font-size: 38px; font-weight: 600; }
  .value-number { font-size: 30px; font-weight: 700; }
  .value-label { font-size: 31px; font-weight: 600; }
</style>
</head>
<body>
<main class="wall-canvas">
  <svg class="values-sign" viewBox="150 320 580 815" xmlns="http://www.w3.org/2000/svg" aria-label="Core values: Safety, Integrity, Quality, Client-Focused Solutions, Continuous Improvement, Positive Culture and Stewardship">
    <defs>
      <linearGradient id="header-fill" x1="0" y1="0" x2="0" y2="1">
        <stop offset="0" stop-color="var(--header-top)"/>
        <stop offset="1" stop-color="var(--header-bottom)"/>
      </linearGradient>
      <linearGradient id="blue-bar" x1="0" y1="0" x2="0" y2="1">
        <stop offset="0" stop-color="var(--blue-light)"/>
        <stop offset="1" stop-color="var(--blue-dark)"/>
      </linearGradient>
      <linearGradient id="blue-fold" x1="0" y1="0" x2="0" y2="1">
        <stop offset="0" stop-color="var(--blue-fold-top)"/>
        <stop offset="1" stop-color="var(--blue-fold-bottom)"/>
      </linearGradient>
      <linearGradient id="red-bar" x1="0" y1="0" x2="0" y2="1">
        <stop offset="0" stop-color="var(--red-light)"/>
        <stop offset="1" stop-color="var(--red-dark)"/>
      </linearGradient>
      <linearGradient id="red-fold" x1="0" y1="0" x2="0" y2="1">
        <stop offset="0" stop-color="var(--red-fold-top)"/>
        <stop offset="1" stop-color="var(--red-fold-bottom)"/>
      </linearGradient>

      <g id="blue-ribbon">
        <rect x="162" y="0" width="53" height="92" fill="url(#blue-bar)"/>
        <polygon points="215,0 260,42 260,138 215,92" fill="url(#blue-fold)"/>
        <rect x="260" y="42" width="306" height="96" fill="url(#blue-bar)"/>
      </g>
      <g id="red-ribbon">
        <rect x="162" y="0" width="53" height="92" fill="url(#red-bar)"/>
        <polygon points="215,0 260,42 260,138 215,92" fill="url(#red-fold)"/>
        <rect x="260" y="42" width="306" height="96" fill="url(#red-bar)"/>
      </g>
    </defs>

    <g class="mission-header">
      <polygon points="216,376 262,330 716,330 716,468 668,514 216,514" fill="url(#header-fill)"/>
      <text class="mission-text" x="468" y="385">Our vision/mission</text>
      <text class="mission-text" x="468" y="424">statement is</text>
      <text class="mission-text" x="468" y="464">Excellence Delivered.</text>
    </g>

    <g class="value-ribbon" transform="translate(0,447)">
      <use href="#blue-ribbon"/>
      <text class="value-number" x="187" y="58">1</text>
      <text class="value-label" x="412" y="100">Safety</text>
    </g>
    <g class="value-ribbon" transform="translate(0,555)">
      <use href="#red-ribbon"/>
      <text class="value-number" x="187" y="58">2</text>
      <text class="value-label" x="412" y="100">Integrity</text>
    </g>
    <g class="value-ribbon" transform="translate(0,663)">
      <use href="#blue-ribbon"/>
      <text class="value-number" x="187" y="58">3</text>
      <text class="value-label" x="412" y="100">Quality</text>
    </g>
    <g class="value-ribbon" transform="translate(0,771)">
      <use href="#red-ribbon"/>
      <text class="value-number" x="187" y="58">4</text>
      <text class="value-label" x="412" y="88">Client-Focused</text>
      <text class="value-label" x="412" y="120">Solutions</text>
    </g>
    <g class="value-ribbon" transform="translate(0,879)">
      <use href="#blue-ribbon"/>
      <text class="value-number" x="187" y="58">5</text>
      <text class="value-label" x="412" y="84">Continuous</text>
      <text class="value-label" x="412" y="116">Improvement</text>
    </g>
    <g class="value-ribbon" transform="translate(0,987)">
      <use href="#red-ribbon"/>
      <text class="value-number" x="187" y="58">6</text>
      <text class="value-label" x="412" y="85">Positive Culture</text>
      <text class="value-label" x="412" y="117">and Stewardship</text>
    </g>
  </svg>
</main>
</body>
</html>
```